Stationary and business card for an electrical contractor
Norvik Electric LLC
Stationary and business card for an electrical contractor - Construction
Creative Brief
Simple
Glen Hadley
President
412 N Orchard Ave
glen@norvikelectric-example.biz
WA Cont. # NORVIEL352TQ

```html
<!DOCTYPE html>
<html lang="en">
<head>
<meta charset="utf-8">
<title>Norvik Electric LLC – Business Card</title>
<link href="https://fonts.googleapis.com/css2?family=Open+Sans:wght@400;600;800&display=swap" rel="stylesheet">
<style>
  :root {
    --bg: #8e8e8e;
    --card-dark: #0d0d0d;
    --card-light: #ffffff;
    --ink: #111111;
    --red: #e0102a;
    --muted: #333333;
  }
  * { margin: 0; padding: 0; box-sizing: border-box; }
  html, body {
    width: 1200px; height: 908px; overflow: hidden;
    background: var(--bg);
    font-family: "Open Sans", Arial, sans-serif;
  }
  .canvas { position: relative; width: 1200px; height: 908px; }
  .card {
    position: absolute;
    width: 600px; height: 343px;
    border-radius: 22px;
    overflow: hidden;
    box-shadow: 0 14px 30px rgba(0,0,0,.35);
  }
  .card--back { left: 120px; top: 70px; background: var(--card-dark); }
  .card--front { left: 480px; top: 490px; background: var(--card-light); }

  .brand {
    display: flex; align-items: center; gap: 12px;
    font-weight: 800; letter-spacing: .5px; text-transform: uppercase;
  }
  .brand__dot { width: 18px; height: 18px; border-radius: 50%; background: var(--red); flex: none; }
  .card--back .brand {
    position: absolute; left: 50%; top: 50%; transform: translate(-50%, -50%);
    color: #ffffff; font-size: 44px; white-space: nowrap;
  }
  .card--front .brand {
    position: absolute; left: 40px; top: 120px;
    color: var(--ink); font-size: 32px; white-space: nowrap;
  }

  .person { position: absolute; right: 40px; top: 40px; text-align: right; }
  .person__name { font-size: 20px; font-weight: 600; color: var(--ink); }
  .person__title { font-size: 16px; font-weight: 600; color: var(--red); margin-top: 2px; }

  .contact { position: absolute; left: 40px; top: 190px; font-size: 14px; color: var(--muted); line-height: 1.55; }
  .contact__license { color: var(--red); font-size: 12px; font-weight: 600; }
  .contact__row { display: flex; align-items: center; gap: 8px; }
  .contact__icon { width: 15px; height: 15px; flex: none; }

  .corner-accent { position: absolute; left: 0; bottom: 0; width: 60px; height: 60px; }
</style>
</head>
<body>
<div class="canvas">

  <section class="card card--back" aria-label="Card back">
    <div class="brand"><span class="brand__dot"></span>Norvik Electric</div>
  </section>

  <section class="card card--front" aria-label="Card front">
    <div class="person">
      <div class="person__name">Glen Hadley</div>
      <div class="person__title">President</div>
    </div>

    <div class="brand"><span class="brand__dot"></span>Norvik Electric</div>

    <div class="contact">
      <div class="contact__license">WA Cont. # NORVIEL352TQ</div>
      <div>412 N Orchard Ave</div>
      <div class="contact__row">
        <svg class="contact__icon" viewBox="0 0 16 16" aria-hidden="true">
          <circle cx="8" cy="8" r="7" fill="none" stroke="var(--red)" stroke-width="1.3"/>
          <path d="M5.5 4.5l1.5 1.2-.7 1.2c.5 1 1.3 1.8 2.3 2.3l1.2-.7 1.2 1.5-.9 1c-2.8-.3-5.2-2.7-5.5-5.5z" fill="var(--red)"/>
        </svg>
        360 555 0147
      </div>
      <div class="contact__row">
        <svg class="contact__icon" viewBox="0 0 16 16" aria-hidden="true">
          <circle cx="8" cy="8" r="7" fill="none" stroke="var(--red)" stroke-width="1.3"/>
          <rect x="4" y="5.3" width="8" height="5.4" fill="none" stroke="var(--red)" stroke-width="1"/>
          <path d="M4 5.5l4 3 4-3" fill="none" stroke="var(--red)" stroke-width="1"/>
        </svg>
        glen@norvikelectric-example.biz
      </div>
    </div>

    <svg class="corner-accent" viewBox="0 0 60 60" aria-hidden="true">
      <path d="M0 0 Q0 60 60 60 L0 60 Z" fill="var(--card-dark)"/>
    </svg>
  </section>

</div>
</body>
</html>
```